Business Card Design Project

We need a new business card design to go along with the look of our new website. tolvarex.com We manufacture after market woodworking machinery parts. Please take a look at the colors on our website and use the same.

Industry/Entity Type

Woodworking

```html
<!DOCTYPE html>
<html lang="en">
<head>
<meta charset="utf-8">
<title>Tolvarex Parts Inc. – Business Card</title>
<link href="https://fonts.googleapis.com/css2?family=PT+Sans:wght@400;700&display=swap" rel="stylesheet">
<style>
  :root {
    --green-dark: #0f6b2c;
    --green: #16873a;
    --green-light: #2aa24f;
    --white: #ffffff;
    --ink-green: #1a7a36;
    --stage: #e4e4e2;
    --brand-grey: #9a9a9a;
  }
  * { margin: 0; padding: 0; box-sizing: border-box; }
  html, body { width: 1200px; height: 725px; overflow: hidden; }
  body {
    background: var(--stage);
    font-family: "PT Sans", Arial, sans-serif;
    position: relative;
  }
  .brand-mark {
    position: absolute; left: 40px; top: 40px;
    display: flex; align-items: center; gap: 12px;
    color: var(--brand-grey); font-weight: 700; font-size: 26px; letter-spacing: 0.5px;
  }
  .brand-mark .dot { width: 18px; height: 18px; border-radius: 50%; background: var(--brand-grey); }

  .card { position: absolute; overflow: hidden; box-shadow: 0 6px 16px rgba(0,0,0,0.18); }
  .card-back {
    left: 600px; top: 80px; width: 540px; height: 300px;
    background: linear-gradient(180deg, var(--green-light) 0%, var(--green) 45%, var(--green-dark) 100%);
  }
  .card-back .band {
    position: absolute; left: 0; right: 0; height: 60px;
    background: linear-gradient(180deg, rgba(255,255,255,0.10), rgba(255,255,255,0));
  }
  .card-back .band-top { top: 20px; }
  .card-back .band-bottom { top: 200px; }
  .card-back .company {
    position: absolute; left: 0; right: 0; top: 128px;
    display: flex; justify-content: center; align-items: center; gap: 14px;
    color: var(--white); font-weight: 700; font-size: 34px; letter-spacing: 1px;
  }
  .card-back .company .dot { width: 22px; height: 22px; border-radius: 50%; background: var(--white); }

  .card-front {
    left: 180px; top: 350px; width: 560px; height: 320px;
    background: var(--white);
  }
  .card-front svg { position: absolute; inset: 0; }
  .card-front .tag-company {
    position: absolute; right: 18px; top: 30px;
    color: var(--white); font-weight: 700; font-size: 15px;
  }
  .holder { position: absolute; left: 40px; top: 42px; color: var(--ink-green); }
  .holder .name { font-size: 30px; font-weight: 400; letter-spacing: 1px; }
  .holder .role { font-size: 10px; letter-spacing: 4px; margin-left: 46px; }
  .address {
    position: absolute; left: 22px; top: 150px;
    color: var(--ink-green); font-size: 15px; line-height: 20px;
  }
  .contacts {
    position: absolute; left: 330px; top: 186px;
    color: var(--ink-green); font-size: 14px; line-height: 20px;
  }
  .web {
    position: absolute; left: 0; right: 0; bottom: 12px; text-align: center;
    color: var(--white); font-weight: 700; font-size: 15px; letter-spacing: 0.5px;
  }
</style>
</head>
<body>
  <div class="brand-mark"><span class="dot"></span><span>TOLVAREX PARTS INC.</span></div>

  <section class="card card-back">
    <div class="band band-top"></div>
    <div class="band band-bottom"></div>
    <div class="company"><span class="dot"></span><span>TOLVAREX PARTS INC.</span></div>
  </section>

  <section class="card card-front">
    <svg width="560" height="320" viewBox="0 0 560 320" aria-hidden="true">
      <defs>
        <linearGradient id="greenFill" x1="0" y1="0" x2="0" y2="1">
          <stop offset="0" stop-color="#2aa24f"/>
          <stop offset="1" stop-color="#0f6b2c"/>
        </linearGradient>
      </defs>
      <path d="M0,0 H560 V78 H420 C380,78 372,16 330,12 H0 Z" fill="url(#greenFill)"/>
      <path d="M0,262 C110,262 150,282 240,282 H560 V320 H0 Z" fill="url(#greenFill)"/>
    </svg>
    <div class="tag-company">TOLVAREX PARTS INC.</div>
    <div class="holder">
      <div class="name">MARTIN HALDER</div>
      <div class="role">MANAGER</div>
    </div>
    <div class="address">
      Tolvarex Parts<br>
      2280 Cedar Ridge Road #310<br>
      Alder Falls CA 90412 USA
    </div>
    <div class="contacts">
      Toll Free : 800.555.0148<br>
      Phone : 555.310.4482<br>
      Fax : 555.310.4490
    </div>
    <div class="web">www.tolvarex.com</div>
  </section>
</body>
</html>
```